Business Card Design Project - The Kernel Harbor

Company Name - The Kernel Harbor

We need a unique logo and business cards

We are a team of experienced IT professionals who specialize in providing business value to organizations via the analysis and understanding the challenges of your particular organization. We focus on understanding the challenges first, and execute against your priorities partnering with your highly valued key resources.

Our extensive experience and focus on Agile delivery methodologies help our clients continuously improve and deliver quality solutions. Using this approach we will always deliver the greatest return on your investments.

Target Market(s)

Large organizations IT departments

Industry/Entity Type

Business

Font styles to use
Serif
Sans Serif

Requirements
Should not have
• no pictures

```html
<!DOCTYPE html>
<html lang="en">
<head>
<meta charset="utf-8">
<title>The Kernel Harbor — Business Cards</title>
<link rel="stylesheet" href="https://fonts.googleapis.com/css2?family=Open+Sans:wght@400;600&display=swap">
<style>
  :root {
    --stage: #1c1c1d;
    --paper: #ffffff;
    --paper-shade: #f1f1f1;
    --teal: #2aa9b3;
    --teal-dark: #1f8e97;
    --slate: #3a3a3c;
    --slate-light: #55565a;
    --slate-dark: #2a2a2c;
    --ink-light: #e9e9e9;
  }
  * { margin: 0; padding: 0; box-sizing: border-box; }
  html, body {
    width: 1200px; height: 863px; overflow: hidden;
    background: var(--stage);
    font-family: "Open Sans", Arial, sans-serif;
  }
  .canvas { position: relative; width: 1200px; height: 863px; }

  .card {
    position: absolute; width: 620px; height: 354px;
    background: linear-gradient(180deg, var(--paper) 0%, var(--paper-shade) 100%);
    overflow: hidden;
    box-shadow: 0 14px 30px rgba(0,0,0,.55);
  }
  .card--front { left: 150px; top: 48px; }
  .card--back  { left: 430px; top: 460px; }

  /* brand */
  .brand { display: flex; align-items: center; gap: 12px; }
  .brand__dot {
    width: 26px; height: 26px; border-radius: 50%;
    background: var(--teal);
  }
  .brand__name {
    color: var(--teal); font-weight: 600; text-transform: uppercase;
    letter-spacing: .18em; font-size: 22px;
  }

  /* key strip */
  .keys {
    position: absolute; left: 0; right: 0; height: 20px;
    display: flex;
  }
  .keys span { flex: 1; background: linear-gradient(180deg, var(--slate-light), var(--slate-dark)); }
  .keys span:nth-child(odd) { background: linear-gradient(180deg, var(--teal), var(--teal-dark)); }

  .band {
    position: absolute; left: 0; right: 0; bottom: 0;
    background: linear-gradient(180deg, var(--slate-light) 0%, var(--slate) 45%, var(--slate-dark) 100%);
  }

  /* front */
  .card--front .brand { position: absolute; left: 0; right: 0; top: 110px; justify-content: center; }
  .card--front .keys { top: 236px; }
  .card--front .band { top: 256px; display: flex; align-items: center; justify-content: center; }
  .website {
    color: var(--ink-light); font-size: 15px; letter-spacing: .2em;
  }

  /* back */
  .card--back .brand { position: absolute; left: 40px; top: 62px; }
  .card--back .brand__name { font-size: 19px; }
  .card--back .keys { top: 140px; }
  .card--back .band { top: 160px; }

  .person { position: absolute; left: 0; bottom: 48px; display: flex; align-items: center; gap: 16px; }
  .person__tab { width: 34px; height: 46px; background: var(--teal); }
  .person__name { color: #fff; font-size: 19px; font-weight: 600; letter-spacing: .04em; text-transform: uppercase; }
  .person__role { color: var(--ink-light); font-size: 13px; letter-spacing: .06em; text-transform: uppercase; }

  .divider { position: absolute; left: 330px; top: 22px; bottom: 22px; width: 1px; background: rgba(255,255,255,.55); }

  .contacts { position: absolute; left: 350px; top: 22px; list-style: none; }
  .contacts li {
    display: flex; align-items: center; gap: 10px;
    color: var(--ink-light); font-size: 13px; height: 28px;
  }
  .contacts svg { width: 15px; height: 15px; flex: none; }
</style>
</head>
<body>
<main class="canvas">

  <section class="card card--front" aria-label="Business card front">
    <div class="brand">
      <span class="brand__dot"></span>
      <span class="brand__name">The Kernel Harbor</span>
    </div>
    <div class="keys"><span></span><span></span><span></span><span></span><span></span><span></span><span></span><span></span><span></span></div>
    <div class="band">
      <p class="website">www.kernelharbor.com</p>
    </div>
  </section>

  <section class="card card--back" aria-label="Business card back">
    <div class="brand">
      <span class="brand__dot"></span>
      <span class="brand__name">The Kernel Harbor</span>
    </div>
    <div class="keys"><span></span><span></span><span></span><span></span><span></span><span></span><span></span><span></span><span></span></div>
    <div class="band">
      <div class="person">
        <span class="person__tab"></span>
        <div>
          <p class="person__name">Daniel Moreau</p>
          <p class="person__role">General Manager</p>
        </div>
      </div>
      <span class="divider"></span>
      <ul class="contacts">
        <li>
          <svg viewBox="0 0 16 16" fill="none" stroke="#e9e9e9" stroke-width="1.4"><rect x="4" y="1" width="8" height="14" rx="1.5"/><line x1="7" y1="12.5" x2="9" y2="12.5"/></svg>
          020 555 0148
        </li>
        <li>
          <svg viewBox="0 0 16 16" fill="#e9e9e9"><path d="M3.5 1.5l2.5-.5 1.5 3.5-1.7 1.2a8 8 0 0 0 4.5 4.5l1.2-1.7 3.5 1.5-.5 2.5c-.3 1-1.2 1.5-2.2 1.4C6.8 13.4 2.6 9.2 2.1 3.7c-.1-1 .4-1.9 1.4-2.2z"/></svg>
          020 555 0148
        </li>
        <li>
          <svg viewBox="0 0 16 16" fill="none" stroke="#e9e9e9" stroke-width="1.4"><rect x="1.5" y="3.5" width="13" height="9" rx="1"/><polyline points="1.5,4 8,9 14.5,4"/></svg>
          hello@kernelharbor.com
        </li>
        <li>
          <svg viewBox="0 0 16 16" fill="none" stroke="#e9e9e9" stroke-width="1.3"><circle cx="8" cy="8" r="6.5"/><ellipse cx="8" cy="8" rx="2.8" ry="6.5"/><line x1="1.5" y1="8" x2="14.5" y2="8"/></svg>
          www.kernelharbor.com
        </li>
        <li>
          <svg viewBox="0 0 16 16" fill="#e9e9e9"><path d="M8 1a5 5 0 0 0-5 5c0 3.8 5 9 5 9s5-5.2 5-9a5 5 0 0 0-5-5zm0 7a2 2 0 1 1 0-4 2 2 0 0 1 0 4z"/></svg>
          41, 9th floor, Quay Point Road
        </li>
      </ul>
    </div>
  </section>

</main>
</body>
</html>
```